Architecture firm needing a business card

We need a business card design for a new company based in the US called "Pellmore Architecture". Seeking minimalist designs that have a creativity/design feel but must be clean and professional. Please refer to the logo attached.

Target Market(s)

Real Estate Investors, Home Builders and Construction Firms.

Industry/Entity Type

Architecture

Contact Information for Business Card

Standard US size business cards. Would like to have some sort of graphic on the back side of the card - nothing that is too loud but something that may catch your attention. More or less grayscale colors that are in line with the logo colors (navy and greys essentially). Additional colors maybe accepted if blended properly (earthtones), but might be difficult to accomplish and maintain the clean/minimalist look.

Requirements
Must have
• Clean Lines
Nice to have
• some sort of graphics, would like to have something creative on the back side of the card
Should not have
• nothing too busy, cluttered or overwhelming.

```html
<!DOCTYPE html>
<html lang="en">
<head>
<meta charset="utf-8">
<title>Pellmore Architecture — Business Card</title>
<link href="https://fonts.googleapis.com/css2?family=Josefin+Sans:wght@300;400;700&family=PT+Serif:wght@400;700&display=swap" rel="stylesheet">
<style>
  :root{
    --page:#ececec;
    --navy:#0f3567;
    --blue:#2f5f9e;
    --grey:#9a9a9a;
    --grey-light:#d2d2d2;
    --grey-mid:#bdbdbd;
    --charcoal:#1c1d1f;
    --white:#ffffff;
  }
  html,body{margin:0;padding:0;overflow:hidden;}
  body{
    width:1200px;height:799px;background:var(--page);
    position:relative;font-family:"Josefin Sans",sans-serif;
  }
  .card{
    position:absolute;width:490px;height:280px;overflow:hidden;
    box-shadow:0 6px 18px rgba(0,0,0,.12);
  }
  .card svg{position:absolute;inset:0;}

  /* Back side */
  .card--back{left:80px;top:260px;background:var(--grey-light);}
  .back-wordmark{
    position:absolute;left:130px;top:112px;color:var(--blue);line-height:1;
  }
  .back-wordmark .line-main{display:block;font-size:42px;font-weight:400;letter-spacing:1px;}
  .back-wordmark .line-sub{display:block;font-size:14px;letter-spacing:8px;margin-top:6px;padding-left:52px;color:var(--grey);}

  /* Front side */
  .card--front{left:630px;top:260px;background:var(--white);}
  .front-wordmark{position:absolute;left:34px;top:40px;color:var(--navy);line-height:1;}
  .front-wordmark .line-main{display:block;font-size:40px;letter-spacing:1px;}
  .front-wordmark .line-sub{display:block;font-size:13px;letter-spacing:8px;margin-top:5px;padding-left:40px;}
  .person{position:absolute;right:30px;top:116px;text-align:right;color:var(--navy);}
  .person .first{font-weight:300;font-size:22px;}
  .person .last{font-weight:700;font-size:22px;}
  .person .role{display:block;font-family:"PT Serif",serif;font-size:9px;color:var(--grey);margin-top:2px;}
  .contact{position:absolute;left:340px;font-family:"PT Serif",serif;color:var(--white);line-height:1.35;}
  .contact--address{top:173px;font-size:11px;font-weight:700;}
  .contact--phone{top:217px;font-size:11px;font-weight:700;}
  .contact--web{top:243px;font-size:9.5px;}
</style>
</head>
<body>

<section class="card card--back" aria-label="Card back">
  <svg width="490" height="280" viewBox="0 0 490 280">
    <path d="M0 40 Q245 -10 490 40 L490 240 Q245 290 0 240 Z" fill="var(--charcoal)"/>
    <path d="M0 40 Q245 -10 490 40" fill="none" stroke="var(--blue)" stroke-width="4"/>
    <path d="M0 240 Q245 290 490 240" fill="none" stroke="var(--blue)" stroke-width="4"/>
    <rect x="0" y="84" width="125" height="8" fill="var(--grey-mid)"/>
    <rect x="0" y="92" width="125" height="3" fill="var(--blue)"/>
    <rect x="395" y="186" width="95" height="8" fill="var(--grey-mid)"/>
    <rect x="395" y="183" width="95" height="3" fill="var(--blue)"/>
    <rect x="100" y="120" width="18" height="18" fill="var(--blue)"/>
  </svg>
  <div class="back-wordmark">
    <span class="line-main">PELLMORE</span>
    <span class="line-sub">ARCHITECTURE</span>
  </div>
</section>

<section class="card card--front" aria-label="Card front">
  <svg width="490" height="280" viewBox="0 0 490 280">
    <polygon points="170,280 250,165 490,165 490,280" fill="var(--navy)"/>
    <polygon points="200,280 280,165 330,165 250,280" fill="var(--grey-light)"/>
    <polygon points="170,280 250,165 262,165 182,280" fill="var(--grey-mid)"/>
    <line x1="330" y1="211" x2="480" y2="211" stroke="var(--white)" stroke-width="1"/>
    <line x1="318" y1="238" x2="480" y2="238" stroke="var(--white)" stroke-width="1"/>
    <g fill="var(--navy)">
      <polygon points="280,188 292,178 304,188"/>
      <rect x="284" y="188" width="16" height="10"/>
    </g>
    <path d="M254 214 q-4 6 2 14 q6 6 12 2 l-3 -4 q-3 2 -6 -1 q-3 -3 -1 -6 z" fill="var(--navy)"/>
    <g fill="none" stroke="var(--navy)" stroke-width="1.5">
      <rect x="226" y="246" width="22" height="15"/>
      <line x1="237" y1="261" x2="237" y2="266"/>
    </g>
  </svg>
  <div class="front-wordmark">
    <span class="line-main">PELLMORE</span>
    <span class="line-sub">ARCHITECTURE</span>
  </div>
  <div class="person">
    <span class="first">Marcus</span><span class="last">REED</span>
    <span class="role">Director</span>
  </div>
  <div class="contact contact--address">418 Alder Ave.<br>Portland, Oregon.</div>
  <div class="contact contact--phone">(503) 555 0142</div>
  <div class="contact contact--web">info@pellmorearchitecture.com<br>www.pellmorearchitecture.com</div>
</section>

</body>
</html>
```